Business card with professional look

I would like a creative yet professional looking business card for our business. We sell broadcast TV related security products for mobile phones, set top boxes, and tablets. Our customers are international. We have a logo we like and I would like to possibly add some color to the business card but keep it professional looking.

Target Market(s)

Professionals in the TV, cable, ans Satellite industries

Industry/Entity Type

Cable Tv

Contact Information for Business Card

Name Ned Vastermill, title CEO, Address 8130 Harborline Court, Suite 400, Del Arvo, CA 91584 USA, phone numbers m:+1.619.284.7302 o:+1.855.672.9140, email, logo

Font styles to use
Other font styles liked:
• Open to any font that looks good with logo

Requirements
Must have
• professional look with colors coordinated with logo colors. would like to add one or two different colors as well as some form of background color

```html
<!DOCTYPE html>
<html lang="en">
<head>
<meta charset="utf-8">
<title>GuardCast Business Card</title>
<link rel="stylesheet" href="https://fonts.googleapis.com/css2?family=Open+Sans:wght@400;600;700;800&display=swap">
<style>
  :root {
    --stage: #000000;
    --card-front: #ffffff;
    --card-back-top: #5a5b5d;
    --card-back-bottom: #1c1c1d;
    --brand-blue: #1560b0;
    --rule-blue: #2a8fd6;
    --ink: #1f1f1f;
    --logo-grey: #3e3f42;
    --logo-white: #ffffff;
  }
  * { margin: 0; padding: 0; box-sizing: border-box; }
  html, body {
    width: 1200px; height: 900px; overflow: hidden;
    background: var(--stage);
    font-family: "Open Sans", sans-serif;
  }
  .stage { position: relative; width: 1200px; height: 900px; }
  .card {
    position: absolute; top: 306px; width: 440px; height: 271px;
    border-radius: 10px; overflow: hidden;
  }
  .card--front { left: 149px; background: var(--card-front); }
  .card--back {
    left: 608px; width: 441px; height: 272px;
    background: linear-gradient(to bottom, var(--card-back-top), var(--card-back-bottom));
  }
  .brand {
    position: absolute; display: flex; align-items: center; gap: 8px;
    font-weight: 700; letter-spacing: -1px; line-height: 1;
  }
  .brand__mark { display: block; background: var(--brand-blue); border-radius: 3px; }
  .card--front .brand {
    right: 26px; top: 60px; font-size: 40px; color: var(--logo-grey);
  }
  .card--front .brand__mark { width: 22px; height: 22px; }
  .card--back .brand {
    left: 0; right: 0; top: 136px; transform: translateY(-50%);
    justify-content: center; font-size: 52px; color: var(--logo-white);
  }
  .card--back .brand__mark { width: 28px; height: 28px; }
  .holder {
    position: absolute; left: 23px; top: 151px;
    display: flex; align-items: baseline; gap: 4px; color: var(--brand-blue);
  }
  .holder__name { font-size: 16px; font-weight: 700; }
  .holder__sep { font-size: 17px; font-weight: 400; }
  .holder__title { font-size: 12px; font-weight: 600; }
  .rule {
    position: absolute; left: 0; right: 0; top: 181px; height: 1.5px;
    background: var(--rule-blue);
  }
  .contact {
    position: absolute; left: 23px; top: 197px;
    font-size: 11.5px; color: var(--ink); line-height: 23px;
  }
  .contact__label { color: var(--brand-blue); font-weight: 700; }
  .contact__divider { margin: 0 5px; }
</style>
</head>
<body>
<main class="stage">
  <section class="card card--front" aria-label="Business card front">
    <div class="brand"><span>GuardCast</span><span class="brand__mark"></span></div>
    <p class="holder">
      <span class="holder__name">Ned Vastermill</span>
      <span class="holder__sep">|</span>
      <span class="holder__title">CEO</span>
    </p>
    <div class="rule"></div>
    <div class="contact">
      <p>8130 Harborline Court, Suite 400, Del Arvo, CA 91584 USA,</p>
      <p>
        <span class="contact__label">T:</span> +1.619.284.7302<span class="contact__divider">|</span>
        <span class="contact__label">C:</span> +1.855.672.9140<span class="contact__divider">|</span>
        <span class="contact__label">E:</span> info@guardcast.com
      </p>
    </div>
  </section>
  <section class="card card--back" aria-label="Business card back">
    <div class="brand"><span>GuardCast</span><span class="brand__mark"></span></div>
  </section>
</main>
</body>
</html>
```